11 x 11 Flyer Design for Social Media - Reverse Mortgages

62 or older?

A Reverse Mortgage
could be
Your Road to Financial Freedom

* No Monthly Payments
* No Income Requirements
* No Credit Score Requirements
* No Loss of Ownership

Receive cash by lump sum, monthly installments or a line of credit!!

Call us today for a Free Consultation!!
(800) 471-2965

Bluegate Financial Services, Inc.
NMLS #318760
www.bluegatehome.com

```html
<!DOCTYPE html>
<html lang="en">
<head>
<meta charset="utf-8">
<title>Reverse Mortgage Flyer – Bluegate Financial Services</title>
<link rel="stylesheet" href="https://fonts.googleapis.com/css2?family=Anton&family=Roboto:wght@300;400;500;700&display=swap">
<style>
  :root {
    --page-bg: #e4e4e4;
    --paper: #f6f6f6;
    --brand-blue: #1a5e86;
    --deep-blue: #1c5a9a;
    --leaf-green: #a4cf3a;
    --pale-green: #eaf6c9;
    --ink: #262626;
    --white: #ffffff;
    --photo-a: #8a96a0;
    --photo-b: #d7dde2;
  }
  * { box-sizing: border-box; margin: 0; padding: 0; }
  html, body { width: 778px; height: 1200px; overflow: hidden; }
  body {
    background: var(--page-bg);
    font-family: "Roboto", Arial, sans-serif;
    position: relative;
  }
  .flyer {
    position: absolute;
    left: 19px; top: 234px;
    width: 740px; height: 732px;
    background: var(--paper);
    overflow: hidden;
    box-shadow: 0 8px 22px rgba(0,0,0,.35);
  }
  .brand {
    position: absolute;
    left: 24px; top: 44px;
    display: flex; align-items: center; gap: 10px;
  }
  .brand-dot {
    width: 38px; height: 38px; border-radius: 50%;
    background: var(--deep-blue);
    flex: none;
  }
  .brand-name {
    font-weight: 500; font-size: 17px; line-height: 1.25;
    color: var(--deep-blue);
    width: 150px;
  }
  .headline {
    position: absolute;
    right: 18px; top: 22px;
    font-family: "Anton", Impact, sans-serif;
    font-size: 58px; line-height: 1;
    color: var(--leaf-green);
    text-shadow: 3px 3px 0 var(--ink);
    letter-spacing: 0.5px;
  }
  .subhead {
    position: absolute;
    right: 20px; top: 98px;
    text-align: right;
    font-size: 23px; line-height: 26px;
    color: var(--ink);
    font-weight: 500;
  }
  .subhead .light { font-weight: 300; }
  .torn-edge { position: absolute; left: 0; top: 158px; width: 740px; height: 50px; }
  .blue-band {
    position: absolute; left: 0; top: 204px;
    width: 740px; height: 405px;
    background: var(--brand-blue);
  }
  .benefits {
    position: absolute; left: 45px; top: 290px;
    list-style: none;
    color: var(--white);
    font-size: 25px; line-height: 1;
  }
  .benefits li {
    display: flex; align-items: center; gap: 14px;
    height: 45.5px;
  }
  .tick { width: 18px; height: 18px; flex: none; }
  .payout {
    position: absolute; left: 29px; top: 465px;
    width: 420px;
    color: var(--white);
    font-size: 25px; line-height: 29px;
  }
  .photos { position: absolute; left: 0; top: 0; width: 740px; height: 732px; }
  .call-band {
    position: absolute; left: 0; top: 609px;
    width: 740px; height: 123px;
    background: var(--leaf-green);
    text-align: center;
  }
  .call-title {
    margin-top: 12px;
    font-weight: 700; font-size: 27px; line-height: 28px;
    color: var(--pale-green); letter-spacing: -0.5px;
  }
  .call-sub { font-size: 22px; line-height: 24px; color: var(--ink); }
  .call-phone {
    font-weight: 700; font-size: 29px; line-height: 28px;
    color: var(--deep-blue);
  }
  .call-web { font-size: 16px; line-height: 20px; color: var(--ink); }
</style>
</head>
<body>
  <article class="flyer">
    <header>
      <div class="brand">
        <span class="brand-dot"></span>
        <span class="brand-name">Bluegate Financial Services, Inc.</span>
      </div>
      <h1 class="headline">62 or older?</h1>
      <p class="subhead">A REVERSE MORTGAGE <span class="light">COULD BE</span><br>YOUR ROAD <span class="light">TO</span> FINANCIAL FREEDOM</p>
    </header>

    <svg class="torn-edge" viewBox="0 0 740 50" aria-hidden="true">
      <polygon fill="var(--brand-blue)" points="0,50 0,18 12,14 20,19 33,12 45,17 58,13 70,18 82,14 96,20 108,15 121,19 134,16 146,22 160,17 172,23 185,18 198,24 212,19 224,25 238,21 250,26 263,22 276,27 290,23 302,28 316,24 330,29 342,25 356,30 370,26 384,31 396,27 410,32 424,28 438,33 450,29 464,34 478,30 492,35 504,31 518,36 532,32 546,37 560,33 572,38 586,34 600,39 612,35 626,40 640,36 654,41 668,37 682,42 696,38 710,43 724,39 740,42 740,50"/>
    </svg>

    <section class="blue-band"></section>

    <ul class="benefits">
      <li><svg class="tick" viewBox="0 0 18 18"><circle cx="9" cy="9" r="9" fill="var(--leaf-green)"/><path d="M5 9.3l2.6 2.6L13 6.5" fill="none" stroke="var(--white)" stroke-width="2"/></svg>No Monthly Payments</li>
      <li><svg class="tick" viewBox="0 0 18 18"><circle cx="9" cy="9" r="9" fill="var(--leaf-green)"/><path d="M5 9.3l2.6 2.6L13 6.5" fill="none" stroke="var(--white)" stroke-width="2"/></svg>No Income Requirements</li>
      <li><svg class="tick" viewBox="0 0 18 18"><circle cx="9" cy="9" r="9" fill="var(--leaf-green)"/><path d="M5 9.3l2.6 2.6L13 6.5" fill="none" stroke="var(--white)" stroke-width="2"/></svg>No Credit Score Requirements</li>
      <li><svg class="tick" viewBox="0 0 18 18"><circle cx="9" cy="9" r="9" fill="var(--leaf-green)"/><path d="M5 9.3l2.6 2.6L13 6.5" fill="none" stroke="var(--white)" stroke-width="2"/></svg>No Loss of Ownership</li>
    </ul>
    <p class="payout">Receive cash by lump sum, monthly installments or a line of credit!!</p>

    <svg class="photos" viewBox="0 0 740 732">
      <defs>
        <linearGradient id="photoTone" x1="0" y1="0" x2="1" y2="1">
          <stop offset="0" stop-color="var(--photo-b)"/>
          <stop offset="1" stop-color="var(--photo-a)"/>
        </linearGradient>
      </defs>
      <g transform="translate(594 282)">
        <polygon points="0,-82 71,-41 71,41 0,82 -71,41 -71,-41" fill="var(--leaf-green)"/>
        <polygon points="0,-71 61,-35.5 61,35.5 0,71 -61,35.5 -61,-35.5" fill="var(--white)"/>
        <polygon points="0,-63 54.5,-31.5 54.5,31.5 0,63 -54.5,31.5 -54.5,-31.5" fill="url(#photoTone)" role="img" aria-label="Photo of a smiling senior couple embracing"/>
      </g>
      <g transform="translate(594 526)">
        <polygon points="0,-82 71,-41 71,41 0,82 -71,41 -71,-41" fill="var(--leaf-green)"/>
        <polygon points="0,-71 61,-35.5 61,35.5 0,71 -61,35.5 -61,-35.5" fill="var(--white)"/>
        <polygon points="0,-63 54.5,-31.5 54.5,31.5 0,63 -54.5,31.5 -54.5,-31.5" fill="url(#photoTone)" role="img" aria-label="Photo of a happy senior couple on an outing"/>
      </g>
      <g transform="translate(642 404)">
        <polygon points="0,-82 71,-41 71,41 0,82 -71,41 -71,-41" fill="var(--leaf-green)"/>
        <polygon points="0,-71 61,-35.5 61,35.5 0,71 -61,35.5 -61,-35.5" fill="var(--white)"/>
        <polygon points="0,-63 54.5,-31.5 54.5,31.5 0,63 -54.5,31.5 -54.5,-31.5" fill="url(#photoTone)" role="img" aria-label="Photo of a thoughtful senior man"/>
      </g>
    </svg>

    <footer class="call-band">
      <p class="call-title">CALL US TODAY</p>
      <p class="call-sub">for a Free Consultation!!</p>
      <p class="call-phone">(800) 471-2965</p>
      <p class="call-web">www.bluegatehome.com</p>
    </footer>
  </article>
</body>
</html>
```